Sticker(s) for a chase dawn road trip

We need a bumper sticker sz and style design with the word - mkbtrz.
I envision the v with a red heart in it, a black background white lettering...but I'm open to other creative flow.
We have a custom Alberta lic plate with mkbtrz for our 1977 KR van on its way. Could also get fun with a copy of lic plate design.
Please include our website on it as well: mkbtrz.ca
Thank you!!! :)))

```html
<!DOCTYPE html>
<html lang="en">
<head>
<meta charset="utf-8">
<title>mkbtrz bumper sticker options</title>
<link rel="stylesheet" href="https://fonts.googleapis.com/css2?family=Chicle&display=swap">
<style>
  :root {
    --page: #ffffff;
    --sticker: #000000;
    --letter: #ffffff;
    --accent: #d40808;
  }
  html, body {
    margin: 0;
    padding: 0;
    width: 1200px;
    height: 1000px;
    overflow: hidden;
    background: var(--page);
  }
  .sheet {
    position: relative;
    width: 1200px;
    height: 1000px;
  }
  .sticker {
    position: absolute;
    left: 227px;
    width: 741px;
    height: 222px;
    display: block;
  }
  .sticker-1 { top: 25px; }
  .sticker-2 { top: 263px; }
  .sticker-3 { top: 507px; }
  .sticker-4 { top: 750px; }
  .sticker-bg { fill: var(--sticker); }
  .wordmark, .web-address {
    font-family: "Chicle", "Bungee", cursive;
    fill: var(--letter);
  }
  .wordmark { font-size: 172px; }
  .accent-dot { fill: var(--accent); }
</style>
</head>
<body>
<main class="sheet">

  <svg class="sticker sticker-1" viewBox="0 0 741 222" aria-label="mkbtrz sticker, web address centred">
    <rect class="sticker-bg" width="741" height="222"/>
    <text class="wordmark" x="16" y="146" textLength="587" lengthAdjust="spacingAndGlyphs">MKBTRZ</text>
    <circle class="accent-dot" cx="666" cy="92" r="48"/>
    <text class="web-address" x="213" y="212" font-size="44" textLength="310" lengthAdjust="spacingAndGlyphs">MKBTRZ.CA</text>
  </svg>

  <svg class="sticker sticker-2" viewBox="0 0 741 222" aria-label="mkbtrz sticker, large web address">
    <rect class="sticker-bg" width="741" height="222"/>
    <text class="wordmark" x="16" y="146" textLength="587" lengthAdjust="spacingAndGlyphs">MKBTRZ</text>
    <circle class="accent-dot" cx="666" cy="92" r="48"/>
    <text class="web-address" x="195" y="214" font-size="50" textLength="346" lengthAdjust="spacingAndGlyphs">MKBTRZ.CA</text>
  </svg>

  <svg class="sticker sticker-3" viewBox="0 0 741 222" aria-label="mkbtrz sticker, web address right">
    <rect class="sticker-bg" width="741" height="222"/>
    <text class="wordmark" x="16" y="146" textLength="587" lengthAdjust="spacingAndGlyphs">MKBTRZ</text>
    <circle class="accent-dot" cx="666" cy="92" r="48"/>
    <text class="web-address" x="420" y="208" font-size="46" textLength="301" lengthAdjust="spacingAndGlyphs">MKBTRZ.CA</text>
  </svg>

  <svg class="sticker sticker-4" viewBox="0 0 741 222" aria-label="mkbtrz sticker, small web address">
    <rect class="sticker-bg" width="741" height="222"/>
    <text class="wordmark" x="16" y="146" textLength="587" lengthAdjust="spacingAndGlyphs">MKBTRZ</text>
    <circle class="accent-dot" cx="666" cy="92" r="48"/>
    <text class="web-address" x="250" y="204" font-size="34" textLength="233" lengthAdjust="spacingAndGlyphs">MKBTRZ.CA</text>
  </svg>

</main>
</body>
</html>
```